Business card design needed

My business is in Matchmaking. My objective is to find the most compatible partner for my clients....basically I'm in the love and happiness industry bringing two people together for a lasting loving relationship.

I envision the design to be something with 2 people who are in love looking happy or even a silhouette.....I don't really know, I'm open to ideas.....maybe no picture at all, but I want it to be classy :-)

I do have a logo which I will upload. You can also go to my website to give you an idea on the colours and the design if that helps, however the website is not finished yet, it should be up by today or tomorrow. If the website has a heart with swirls on the upper left hand corner, that is the old website, please ignore that one. The one that will be up shortly has a picture frame on the home page with my logo that will be in the file I will upload on this page.

Target Market(s)

There are three categories: Over 45, Asian and Western and same sex, but would be able to afford to hire a matchmaker

Contact Information for Business Card

The Tide Lantern
Helping You Find The "One"
Mira Feltham
Matchmaker
0472 915 264
info@thetidelantern.com.au
www.thetidelantern.com.au

```html
<!DOCTYPE html>
<html lang="en">
<head>
<meta charset="utf-8">
<title>The Tide Lantern – Business Card</title>
<link href="https://fonts.googleapis.com/css2?family=Open+Sans:wght@400;700&display=swap" rel="stylesheet">
<style>
  :root {
    --page-bg: #ece8e6;
    --cream: #fdf0d8;
    --plum: #7b5c79;
    --lilac: #c4b6c6;
    --teal: #7fb8aa;
    --photo-light: #c9cccb;
    --photo-dark: #3a3d3c;
    --white: #ffffff;
  }
  html, body {
    margin: 0;
    width: 1200px;
    height: 1000px;
    overflow: hidden;
    background: var(--page-bg);
    font-family: "Open Sans", Arial, sans-serif;
  }
  .card {
    position: absolute;
    left: 100px;
    top: 214px;
    width: 1000px;
    height: 572px;
    display: flex;
    box-shadow: 0 6px 18px rgba(0,0,0,0.18);
    background: var(--cream);
  }
  .card__photo {
    width: 320px;
    height: 100%;
    background: linear-gradient(135deg, var(--photo-light) 0%, #9a9e9c 50%, var(--photo-dark) 100%);
  }
  .card__divider {
    width: 6px;
    height: 100%;
    background: var(--teal);
  }
  .card__content {
    flex: 1;
    display: flex;
    flex-direction: column;
  }
  .card__brand {
    height: 262px;
    background: var(--cream);
    display: flex;
    flex-direction: column;
    align-items: center;
    justify-content: flex-end;
    padding-bottom: 22px;
    box-sizing: border-box;
  }
  .brand__mark {
    display: flex;
    align-items: center;
    gap: 14px;
    margin-bottom: 10px;
  }
  .brand__dot {
    width: 26px;
    height: 26px;
    border-radius: 50%;
    background: var(--teal);
  }
  .brand__name {
    font-size: 46px;
    font-weight: 400;
    color: var(--plum);
  }
  .brand__tagline {
    font-size: 30px;
    font-weight: 700;
    color: var(--plum);
    letter-spacing: -0.3px;
  }
  .card__details {
    flex: 1;
    background: linear-gradient(90deg, var(--plum) 0%, var(--plum) 62%, var(--lilac) 76%, var(--lilac) 100%);
    color: var(--white);
    padding: 26px 34px;
    box-sizing: border-box;
  }
  .details__name {
    font-size: 44px;
    font-weight: 700;
    line-height: 1.05;
  }
  .details__role {
    font-size: 28px;
    font-weight: 700;
    margin-bottom: 22px;
  }
  .details__contact {
    font-size: 30px;
    font-weight: 700;
    line-height: 1.22;
  }
</style>
</head>
<body>
  <div class="card">
    <div class="card__photo" role="img" aria-label="Black and white photo of two clasped hands, one wearing an engagement ring"></div>
    <div class="card__divider"></div>
    <div class="card__content">
      <div class="card__brand">
        <div class="brand__mark">
          <span class="brand__dot"></span>
          <span class="brand__name">The Tide Lantern</span>
        </div>
        <div class="brand__tagline">Helping You Find The "One"</div>
      </div>
      <div class="card__details">
        <div class="details__name">Mira Feltham</div>
        <div class="details__role">Matchmaker</div>
        <div class="details__contact">Tel. 0472 915 264</div>
        <div class="details__contact">mira@thetidelantern.com.au</div>
        <div class="details__contact">www.thetidelantern.com.au</div>
      </div>
    </div>
  </div>
</body>
</html>
```